Webbanner-Design für Ebook - Unterwegs im Süden Ungarns ( Affiliate und Promivo)
Zielgruppe
Wir verkaufen Ebooks. In diesem Fall möchten wir Kroatien Liebhaber aufmerksam machen, dass es mittlerweile ein Buch gibt, welches all die Sehenswürdigkeiten und Routen bis nach Kroatien ausführlich beschreibt.
Aufgabenstellung
Da wir unseren Affiliate Partner die Möglichkeit geben wollen, unsere Produkte zu verkaufen, benötigen wir diesbezüglich gute Anzeigen mit verschiedener Größen. ( affiliate und Promivo )
Sollten Vorlagen / Stockfotos verwendet werden, dann bitte über bildfang
Ich habe einige Fotos welches wir bereits erworben haben hier hochgeladen.
Auch das Coverbild ist im Anhang.
Ideal wäre eine Buch-Abbildung für die Anzeigen.
3 Anzeigegrößen erforderlich
728 x 90 300 x 250 300 x 600

```html
<!DOCTYPE html>
<html lang="de">
<head>
<meta charset="utf-8">
<title>Unterwegs im Süden Ungarns – EBook Banner</title>
<link href="https://fonts.googleapis.com/css2?family=Arimo:wght@700&family=Anton&display=swap" rel="stylesheet">
<style>
:root{
  --black:#000;
  --orange:#ff9900;
  --yellow:#ffff00;
  --red:#ff0000;
  --sky:#3399ff;
  --navy:#0000b4;
  --white:#fff;
  --ink-orange:#6b3a12;
  --ink-yellow:#5a4d12;
  --cover-top:#4f6aa0;
  --cover-mid:#9bb0c8;
  --cover-sea:#8fa9bf;
  --cover-land:#c9a77a;
  --badge:#d0111b;
  --sign:#1f4fa8;
}
*{box-sizing:border-box;margin:0;padding:0}
html,body{width:1114px;height:1200px;overflow:hidden;background:var(--white)}
body{position:relative;font-family:"Arimo",Arial,sans-serif;font-weight:700}
.banner{position:absolute;overflow:hidden}
.banner--black{left:16px;top:0;width:345px;height:288px;background:var(--black)}
.banner--orange{left:391px;top:3px;width:352px;height:293px;background:var(--orange)}
.banner--yellow{left:759px;top:5px;width:349px;height:291px;background:var(--yellow)}
.banner--face{left:28px;top:375px;width:313px;height:628px;background:var(--red)}
.banner--sky{left:425px;top:394px;width:307px;height:617px;background:var(--sky)}
.banner--red{left:782px;top:396px;width:309px;height:617px;background:var(--red)}
.banner--leader{left:0;top:1063px;width:1114px;height:137px;background:var(--navy)}

.headline{position:absolute;font-size:52px;line-height:1;letter-spacing:-1px;color:var(--white)}
.features{position:absolute;list-style:none;font-size:17px;line-height:18.5px;color:var(--white)}
.features li::before{content:"- "}
.on-orange,.on-yellow{color:var(--black)}
.features.on-orange{color:var(--ink-orange)}
.features.on-yellow{color:var(--ink-yellow)}
.heart{position:absolute;width:93px;height:93px}

.cover{position:absolute;container-type:inline-size;aspect-ratio:2/3;overflow:hidden;
  background:linear-gradient(180deg,var(--cover-top) 0%,var(--cover-mid) 42%,var(--cover-sea) 60%,var(--cover-land) 100%);
  font-family:"Anton","Oswald",sans-serif;color:var(--white);text-transform:uppercase}
.cover__photo{position:absolute;left:0;top:42%;width:100%;height:58%;
  background:linear-gradient(180deg,#b7a38a 0%,#9fb4c6 35%,#8aa3b9 60%,#b9a06c 100%)}
.cover__kicker{position:absolute;left:7%;top:3.5%;font-size:10cqw;line-height:1}
.cover__title{position:absolute;left:6%;top:10%;font-size:19cqw;line-height:.98}
.cover__title small{font-size:10cqw}
.cover__sub{position:absolute;left:7%;top:36%;font-family:"Arimo",Arial,sans-serif;font-weight:700;
  text-transform:none;font-size:4.2cqw;line-height:1.15;color:#e6ecf4}
.cover__badge{position:absolute;right:6%;top:32%;width:30cqw;height:30cqw;border-radius:50%;
  background:var(--badge);display:flex;align-items:center;justify-content:center;text-align:center;
  font-family:"Arimo",Arial,sans-serif;font-size:2.9cqw;line-height:1.2}
.cover__sign{position:absolute;left:8%;top:70%;width:34cqw;height:34cqw;border-radius:2cqw;
  background:var(--sign);border:1cqw solid #e8eef8}
.cover__author{position:absolute;left:43%;bottom:3.5%;font-size:6cqw;text-transform:none}
.photo-face{position:absolute;left:25px;top:0;width:266px;height:163px;
  background:linear-gradient(180deg,#c8201f 0%,#b32020 30%,#d9d9d9 45%,#cfd4da 62%,#2b3f9a 70%,#22338a 100%)}
</style>
</head>
<body>

<svg width="0" height="0" style="position:absolute">
  <defs>
    <linearGradient id="heartFill" x1="0" y1="0" x2="0" y2="1">
      <stop offset="0" stop-color="#e3262b"/>
      <stop offset=".33" stop-color="#e3262b"/>
      <stop offset=".4" stop-color="#ffffff"/>
      <stop offset=".68" stop-color="#f1f1f1"/>
      <stop offset=".75" stop-color="#26388f"/>
      <stop offset="1" stop-color="#1b2b78"/>
    </linearGradient>
    <symbol id="heart" viewBox="0 0 100 100">
      <path d="M50 96 C30 78 4 62 4 32 C4 14 17 4 30 4 C40 4 47 10 50 17 C53 10 60 4 70 4 C83 4 96 14 96 32 C96 62 70 78 50 96 Z" fill="url(#heartFill)"/>
    </symbol>
  </defs>
</svg>

<!-- 300 x 250 black -->
<section class="banner banner--black">
  <div class="cover" style="left:0;top:39px;width:129px">
    <div class="cover__photo" role="img" aria-label="Küstenfoto mit Altstadt und Straße"></div>
    <div class="cover__kicker">Unterwegs</div>
    <div class="cover__title"><small>im</small> Süden<br>Ungarns</div>
    <div class="cover__sub">Der perfekte Guide für<br>Fahrer &amp; Beifahrer</div>
    <div class="cover__badge">Alles über Maut, Tunnel, Camping</div>
    <div class="cover__sign" role="img" aria-label="Verkehrszeichen Mautstelle"></div>
    <div class="cover__author">Jonas Brenner</div>
  </div>
  <div class="headline" style="left:147px;top:22px">EBook</div>
  <ul class="features" style="left:152px;top:95px">
    <li>Mautgebühren</li><li>Tunnelgebühren</li><li>Campingplätze</li><li>Sehenswürdigkeiten</li>
  </ul>
  <svg class="heart" style="left:183px;top:190px" role="img" aria-label="Herz in Landesfarben"><use href="#heart"/></svg>
</section>

<!-- 300 x 250 orange -->
<section class="banner banner--orange">
  <div class="cover" style="left:0;top:40px;width:131px">
    <div class="cover__photo" role="img" aria-label="Küstenfoto mit Altstadt und Straße"></div>
    <div class="cover__kicker">Unterwegs</div>
    <div class="cover__title"><small>im</small> Süden<br>Ungarns</div>
    <div class="cover__sub">Der perfekte Guide für<br>Fahrer &amp; Beifahrer</div>
    <div class="cover__badge">Alles über Maut, Tunnel, Camping</div>
    <div class="cover__sign" role="img" aria-label="Verkehrszeichen Mautstelle"></div>
    <div class="cover__author">Jonas Brenner</div>
  </div>
  <div class="headline on-orange" style="left:149px;top:24px">EBook</div>
  <ul class="features on-orange" style="left:155px;top:100px">
    <li>Mautgebühren</li><li>Tunnelgebühren</li><li>Campingplätze</li><li>Sehenswürdigkeiten</li>
  </ul>
  <svg class="heart" style="left:188px;top:192px" role="img" aria-label="Herz in Landesfarben"><use href="#heart"/></svg>
</section>

<!-- 300 x 250 yellow -->
<section class="banner banner--yellow">
  <div class="cover" style="left:0;top:39px;width:130px">
    <div class="cover__photo" role="img" aria-label="Küstenfoto mit Altstadt und Straße"></div>
    <div class="cover__kicker">Unterwegs</div>
    <div class="cover__title"><small>im</small> Süden<br>Ungarns</div>
    <div class="cover__sub">Der perfekte Guide für<br>Fahrer &amp; Beifahrer</div>
    <div class="cover__badge">Alles über Maut, Tunnel, Camping</div>
    <div class="cover__sign" role="img" aria-label="Verkehrszeichen Mautstelle"></div>
    <div class="cover__author">Jonas Brenner</div>
  </div>
  <div class="headline on-yellow" style="left:149px;top:22px">EBook</div>
  <ul class="features on-yellow" style="left:153px;top:98px">
    <li>Mautgebühren</li><li>Tunnelgebühren</li><li>Campingplätze</li><li>Sehenswürdigkeiten</li>
  </ul>
  <svg class="heart" style="left:186px;top:190px" role="img" aria-label="Herz in Landesfarben"><use href="#heart"/></svg>
</section>

<!-- 300 x 600 with portrait -->
<section class="banner banner--face">
  <div class="photo-face" role="img" aria-label="Foto: Gesicht mit aufgemalter Landesflagge"></div>
  <div class="headline" style="left:0;width:100%;text-align:center;top:190px;font-size:46px">EBook</div>
  <div class="cover" style="left:49px;top:267px;width:225px">
    <div class="cover__photo" role="img" aria-label="Küstenfoto mit Altstadt und Straße"></div>
    <div class="cover__kicker">Unterwegs</div>
    <div class="cover__title"><small>im</small> Süden<br>Ungarns</div>
    <div class="cover__sub">Der perfekte Guide für<br>Fahrer &amp; Beifahrer</div>
    <div class="cover__badge">Alles über Maut, Tunnel, Camping</div>
    <div class="cover__sign" role="img" aria-label="Verkehrszeichen Mautstelle"></div>
    <div class="cover__author">Jonas Brenner</div>
  </div>
</section>

<!-- 300 x 600 sky -->
<section class="banner banner--sky">
  <div class="headline" style="left:0;width:100%;text-align:center;top:24px;font-size:46px">EBook</div>
  <div class="cover" style="left:46px;top:98px;width:221px">
    <div class="cover__photo" role="img" aria-label="Küstenfoto mit Altstadt und Straße"></div>
    <div class="cover__kicker">Unterwegs</div>
    <div class="cover__title"><small>im</small> Süden<br>Ungarns</div>
    <div class="cover__sub">Der perfekte Guide für<br>Fahrer &amp; Beifahrer</div>
    <div class="cover__badge">Alles über Maut, Tunnel, Camping</div>
    <div class="cover__sign" role="img" aria-label="Verkehrszeichen Mautstelle"></div>
    <div class="cover__author">Jonas Brenner</div>
  </div>
  <ul class="features" style="left:24px;top:482px;font-size:24px;line-height:26px">
    <li>Mautgebühren</li><li>Tunnelgebühren</li><li>Campingplätze</li><li>Sehenswürdigkeiten</li>
  </ul>
</section>

<!-- 300 x 600 red -->
<section class="banner banner--red">
  <div class="headline" style="left:0;width:100%;text-align:center;top:26px;font-size:46px">EBook</div>
  <div class="cover" style="left:46px;top:98px;width:221px">
    <div class="cover__photo" role="img" aria-label="Küstenfoto mit Altstadt und Straße"></div>
    <div class="cover__kicker">Unterwegs</div>
    <div class="cover__title"><small>im</small> Süden<br>Ungarns</div>
    <div class="cover__sub">Der perfekte Guide für<br>Fahrer &amp; Beifahrer</div>
    <div class="cover__badge">Alles über Maut, Tunnel, Camping</div>
    <div class="cover__sign" role="img" aria-label="Verkehrszeichen Mautstelle"></div>
    <div class="cover__author">Jonas Brenner</div>
  </div>
  <ul class="features" style="left:24px;top:484px;font-size:24px;line-height:26px">
    <li>Mautgebühren</li><li>Tunnelgebühren</li><li>Campingplätze</li><li>Sehenswürdigkeiten</li>
  </ul>
</section>

<!-- 728 x 90 leaderboard -->
<section class="banner banner--leader">
  <div class="cover" style="left:0;top:3px;width:251px">
    <div class="cover__photo" role="img" aria-label="Küstenfoto mit Altstadt und Straße"></div>
    <div class="cover__kicker">Unterwegs</div>
    <div class="cover__title"><small>im</small> Süden<br>Ungarns</div>
    <div class="cover__sub">Der perfekte Guide für<br>Fahrer &amp; Beifahrer</div>
    <div class="cover__badge">Alles über Maut, Tunnel, Camping</div>
    <div class="cover__sign" role="img" aria-label="Verkehrszeichen Mautstelle"></div>
    <div class="cover__author">Jonas Brenner</div>
  </div>
  <div class="headline" style="left:348px;top:30px;font-size:70px">EBook</div>
  <ul class="features" style="left:651px;top:22px;font-size:20px;line-height:24.5px">
    <li>Mautgebühren</li><li>Tunnelgebühren</li><li>Campingplätze</li><li>Sehenswürdigkeiten</li>
  </ul>
  <svg class="heart" style="left:970px;top:3px;width:124px;height:124px" role="img" aria-label="Herz in Landesfarben"><use href="#heart"/></svg>
</section>

</body>
</html>
```